Specialized Personal Trainer Needs a Business Card Design

I need a business card design for my personal training business called Tall Oak Fitness. I have my Human Kinetics degree in Exercise Science from the Halvern Ridge University as well as an extra certification from NBEP (National Board of Exercise Practice). I work as a Cardiac Rehab Exercise Specialist and personal trainer giving specialized exercise prescriptions to those that have different heart conditions as well as work with the general population in weight loss, strength and conditioning, getting/staying fit.
Updates

I decided that I wanted a logo (as I did not have one before I submitted my project for a business card) so I am submitting a project to get a logo done and then I will decide on a business card, hopefully being able to use one of the designs already submitted.  My apologies for doing this backwards.  I am new to this so I appreciate your patience.

Thank you.

Hi, I have just created a project for a logo design (I realized I needed a logo and I should've done that first..oops!), please feel free to participate.  Once I receive a logo I like I will finalize my business card project and hopefully incorporate it into one of your business card designs. 

Thank you!

Target Market(s)

Business professionals

Industry/Entity Type

Personal Trainer

Requirements
Must have
• My name with my info:
Celia R. Dunhill (BHK)
NBEP Certified Clinical Exercise Specialist & Personal Trainer
celia.dunhill@talloakfitness.example
Cell: 604-358-4170

Please make it double sided.
Nice to have
• An image that represents cardiac and general fitness training.

```html
<!DOCTYPE html>
<html lang="en">
<head>
<meta charset="utf-8">
<title>Tall Oak Fitness – Business Card</title>
<link rel="stylesheet" href="https://fonts.googleapis.com/css2?family=Barlow:wght@400;800&family=Roboto+Condensed:wght@400;700&display=swap">
<style>
  :root {
    --brand-red: #e31937;
    --paper: #ffffff;
    --page: #ffffff;
    --card-edge: #d6d6d6;
    --card-shadow: rgba(0, 0, 0, 0.28);
  }
  * { box-sizing: border-box; margin: 0; padding: 0; }
  html, body {
    width: 1200px;
    height: 901px;
    overflow: hidden;
    background: var(--page);
  }
  .stage {
    position: relative;
    width: 1200px;
    height: 901px;
  }
  .card {
    position: absolute;
    left: 272px;
    width: 664px;
    height: 380px;
    border-radius: 38px;
    overflow: hidden;
    box-shadow: 0 6px 10px var(--card-shadow);
  }
  .card--front {
    top: 56px;
    background: var(--brand-red);
    display: flex;
    align-items: center;
    justify-content: center;
  }
  .wordmark {
    font-family: "Barlow", sans-serif;
    font-weight: 800;
    color: var(--paper);
    text-align: center;
    line-height: 0.92;
    letter-spacing: -1px;
    text-transform: uppercase;
  }
  .wordmark__line { display: block; font-size: 82px; }

  .card--back {
    top: 473px;
    background: var(--paper);
    border: 1px solid var(--card-edge);
    color: var(--brand-red);
    text-align: center;
  }
  .services {
    position: absolute;
    top: 52px;
    left: 0;
    right: 0;
    font-family: "Barlow", sans-serif;
    font-weight: 400;
    font-size: 18px;
    letter-spacing: 1.2px;
    text-transform: uppercase;
  }
  .services__divider { margin: 0 14px; }
  .business-name {
    position: absolute;
    top: 165px;
    left: 0;
    right: 0;
    font-family: "Roboto Condensed", sans-serif;
    font-weight: 700;
    font-size: 35px;
  }
  .trainer-name {
    position: absolute;
    top: 228px;
    left: 0;
    right: 0;
    font-family: "Roboto Condensed", sans-serif;
    font-weight: 700;
    font-size: 25px;
  }
  .trainer-name__degree { font-weight: 400; }
  .trainer-title {
    position: absolute;
    top: 258px;
    left: 0;
    right: 0;
    font-family: "Roboto Condensed", sans-serif;
    font-size: 17px;
  }
  .contact-phone {
    position: absolute;
    top: 299px;
    left: 0;
    right: 0;
    font-family: "Roboto Condensed", sans-serif;
    font-size: 22px;
  }
  .contact-web {
    position: absolute;
    top: 326px;
    left: 0;
    right: 0;
    font-family: "Roboto Condensed", sans-serif;
    font-size: 21px;
    white-space: nowrap;
  }
  .contact-web__gap { display: inline-block; width: 22px; }
</style>
</head>
<body>
  <main class="stage">
    <section class="card card--front" aria-label="Card front">
      <h1 class="wordmark">
        <span class="wordmark__line">Tall Oak</span>
        <span class="wordmark__line">Fitness</span>
      </h1>
    </section>

    <section class="card card--back" aria-label="Card back">
      <p class="services">Training<span class="services__divider">|</span>Cardiac Rehabilitation<span class="services__divider">|</span>Wellness</p>
      <h2 class="business-name">Tall Oak Fitness</h2>
      <p class="trainer-name">Celia R. Dunhill <span class="trainer-name__degree">(BHK)</span></p>
      <p class="trainer-title">NBEP Cert. &amp; Personal Trainer</p>
      <p class="contact-phone">604-358-4170</p>
      <p class="contact-web">celia.dunhill@talloakfitness.example<span class="contact-web__gap"></span>www.talloakfitness.example</p>
    </section>
  </main>
</body>
</html>
```